Online Cooking App Pitch Deck- (THIS IS NOT A FOOD BUSINESS OR FOOD SERVICE, NO FOOD PICTURES)

Project Goal:
Design a visually compelling pitch deck to be used for securing investment. Looking for the pitch deck to be about the design using shapes, colors, fonts and sizes. Must be creative yet simple and clean.
Color Palette:
https://palettrix.example/ff3800-ffe2db-fefefa-2d3e50-010b13

(We want most screens to use #FEFEFA)

This is the current pitch deck we need simplified and redesigned (USE TEXT IN THE GOOGLE LINK TO SHOW IN YOUR DESIGN):

https://slides.vornidex.example/deck/8QmTzR42kLpWx7nHa3Jv-cYdoeBtfGuqN/edit?share=link&uid=592031846720518390417&fmt=true&mode=true

Project is now guaranteed. Remember use the text in the google link in powerpoint design. Use a little more color not just the logo color. Do not use any pictures of food this is not food related business. We care more about style and design of shapes, text, color fonts.

Target Market(s)

Investors (venture capitalists, angel investors) interested in innovative technology solutions within the food industry.

Font styles to use
Serif
Sans Serif

Requirements
Nice to have
• Simple, abstract background non distracting but complementary.
Should not have
• No pictures

```html
<!DOCTYPE html>
<html lang="en">
<head>
<meta charset="utf-8">
<title>Kitchen Duo – Investor Deck Overview</title>
<link href="https://fonts.googleapis.com/css2?family=Poppins:ital,wght@0,400;0,500;0,600;0,700;0,800;1,600;1,700&display=swap" rel="stylesheet">
<style>
:root{
  --orange:#ff3800;
  --blush:#ffe2db;
  --paper:#fefefa;
  --navy:#2d3e50;
  --ink:#010b13;
  --charcoal:#262626;
  --mist:#f0f0ee;
  --body:#666;
  --stage:#e5e5e3;
}
*{box-sizing:border-box;margin:0;padding:0}
html,body{width:905px;height:1200px;overflow:hidden;background:var(--stage)}
.canvas{position:relative;width:905px;height:1200px;overflow:hidden;background:var(--stage);font-family:'Poppins',sans-serif;color:var(--ink)}

.slide{position:absolute;width:271px;height:153px;background:var(--paper);overflow:hidden;box-shadow:0 2px 5px rgba(0,0,0,.22)}
.slide > *{position:absolute}
.slide.dark{background:var(--charcoal);color:#fff}
.c1{left:35px}.c2{left:317px}.c3{left:598px}
.r1{top:33px}.r2{top:196px}.r3{top:359px}.r4{top:524px}.r5{top:688px}.r6{top:850px}.r7{top:1013px}

.tagline{left:6px;top:15px;font-size:3.6px;font-weight:600}
.tagline::before{content:"";position:absolute;left:-6px;top:-.5px;width:2px;height:5px;background:var(--orange)}
.brand{right:10px;top:8px;font-size:6px;font-weight:600;color:var(--ink)}
.dark .brand{color:#fff}
.insight-no{right:10px;top:20px;font-size:5px;font-weight:500}
.confidential{left:6px;bottom:5px;background:#1e1e1e;color:#fff;font-size:2.6px;padding:1px 4px;border-radius:3px;font-weight:500}
.dark .confidential{background:#fff;color:#1e1e1e}
.corner-mark{right:-12px;bottom:-12px;width:32px;height:32px;border-radius:50%;background:var(--orange)}
.page-no{right:5px;bottom:4px;font-size:3.4px;color:#fff;font-weight:600}

.lorem{font-size:2.8px;line-height:1.35;color:var(--body)}
.lorem p+p{margin-top:3px}
.dark .lorem{color:#ddd}
.accent{color:var(--orange)}
.h{font-weight:700;line-height:1.05}
.center{left:0;width:100%;text-align:center}

/* cover */
.cover-title{top:50px;font-size:22px;font-weight:700}
.cover-title sup{font-size:4px;vertical-align:top;margin-left:2px}
.cover-sub{top:90px;font-size:5.2px;font-style:italic;font-weight:700;line-height:1.5}
.waves{left:0;top:0;width:271px;height:153px}
.dots{display:flex;gap:3px}
.dots i{width:3.5px;height:3.5px;border-radius:50%;background:#fff;display:block}
.dots i.on{background:var(--orange)}

.pill{top:96px;left:50%;transform:translateX(-50%);background:var(--orange);color:#fff;font-size:6px;font-weight:500;padding:1px 6px;border-radius:6px;white-space:nowrap}

.boxed{background:var(--orange);color:#fff;padding:0 3px}

/* stats */
.stats{left:38px;top:83px;width:195px;height:39px;background:var(--mist);display:flex}
.stat{flex:1;padding:4px 0 0 10px;border-right:.5px solid #ddd}
.stat:last-child{border:0}
.stat b{display:block;color:var(--orange);font-size:8px;font-weight:700;line-height:1.1}
.stat strong{display:block;font-size:4.6px;font-weight:700}
.stat span{display:block;font-size:2.6px;color:var(--body);line-height:1.3}

/* cards */
.card{width:63px;height:74px;background:#fff;box-shadow:0 1px 3px rgba(0,0,0,.2)}
.card-head{background:#1e1e1e;color:#fff;font-size:8.5px;font-weight:600;height:15px;line-height:15px;padding-left:4px;margin:-3px -2px 0 -2px}
.card .lorem{padding:4px 5px;font-size:2.6px}
.band{background:var(--orange)}

/* solutions */
.ring{left:32px;top:51px;width:58px;height:58px;border:3.5px solid #1e1e1e;border-radius:50%;display:flex;flex-direction:column;align-items:center;justify-content:center;font-size:5.8px;font-weight:700;line-height:1.25}
.item-icon{width:18px;height:18px;border-radius:50%;background:var(--orange);border:1.5px solid var(--blush)}
.item-text{width:92px}
.item-text strong{display:block;font-size:5px;font-weight:600}
.item-text .lorem{font-size:2.5px}

/* better solution */
.step{top:43px;width:43px;height:65px;border:1.6px solid #1e1e1e;border-radius:5px;text-align:center;padding-top:11px}
.step b{display:block;color:var(--orange);font-size:3.8px;font-weight:700;margin:2px 0}
.step .lorem{font-size:2.3px;padding:0 3px}
.node{width:4px;height:4px;border-radius:50%;background:#1e1e1e}

/* demo */
.num{width:9px;height:9px;background:var(--orange);color:#fff;font-size:6px;font-weight:700;text-align:center;line-height:9px}
.demo-item strong{display:block;font-size:4.8px;font-weight:600}
.demo-item .lorem{font-size:2.4px;width:70px}
.phone{width:29px;height:58px;border:1.5px solid #1e1e1e;border-radius:4px;background:#fff;padding:5px 3px;font-size:3px;font-weight:700;line-height:1.2}
.phone .lorem{font-size:1.9px;font-weight:400;margin-top:3px}
.phone .glyph{width:8px;height:6px;border:.6px solid var(--orange);margin:4px auto 0}

/* timeline */
.ribbon{top:84px;width:40px;height:6px;color:#fff;font-size:3.2px;font-weight:600;text-align:center;line-height:6px;clip-path:polygon(4px 0,calc(100% - 4px) 0,100% 100%,0 100%)}
.tl-note{width:50px;text-align:center;font-size:3.4px;font-weight:600}
.tl-note span{display:block;font-weight:400;font-size:2.6px;color:var(--body);line-height:1.25}
.stem{width:.8px;background:#1e1e1e}
.stem.hot{background:var(--orange)}
.stem::after{content:"";position:absolute;left:-1.2px;width:3px;height:3px;border-radius:50%;background:inherit}
.stem.up::after{top:-1px}.stem.down::after{bottom:-1px}

/* revenue */
.rev{width:72px;font-size:3.8px;font-weight:600}
.rev .lorem{font-size:2.4px;font-weight:400}
.rev.left{text-align:right}

/* projections */
.proj{width:43px;text-align:center;font-size:3.6px;font-weight:500}
.proj .lorem{font-size:2.5px;margin-top:2px}

/* ask */
.bullet{width:88px;padding-left:7px;font-size:4.6px;font-weight:600}
.bullet::before{content:"";position:absolute;left:0;top:1.4px;width:3.5px;height:3.5px;border-radius:50%;background:var(--orange)}
.bullet .lorem{font-size:2.4px;font-weight:400}
.ph{background:linear-gradient(160deg,#d9d9d9,#b8b8b8)}

/* team */
.member{top:50px;width:40px;text-align:center}
.member .strip{position:relative;height:16px}
.member .face{position:absolute;left:11px;top:2px;width:18px;height:18px;border-radius:50%;background:linear-gradient(160deg,#cfcfcf,#9e9e9e);border:1px solid #fff}
.member h4{font-size:4.4px;font-weight:700;margin-top:8px}
.member .lorem{font-size:2.3px}

/* contact */
.contact{left:148px;display:flex;gap:5px;align-items:flex-start;font-size:3.8px;line-height:1.3;color:#fff}
.contact svg{flex:none;width:7px;height:7px}
</style>
</head>
<body>
<main class="canvas">

<!-- 1 Cover dark -->
<section class="slide dark c1 r1">
  <svg class="waves" viewBox="0 0 271 153" aria-hidden="true">
    <path d="M140 0 Q168 28 205 17 Q238 7 247 32 Q256 54 271 52 L271 0Z" fill="#d8d8d8"/>
    <path d="M150 0 Q172 22 205 12 Q236 3 246 24 Q256 44 271 42 L271 0Z" fill="#262626"/>
    <path d="M182 0 Q198 14 218 9 Q242 3 252 18 Q261 32 271 30 L271 0Z" fill="#ff3800"/>
    <path d="M150 153 Q168 133 198 139 Q228 145 240 124 Q254 103 271 108 L271 153Z" fill="#ff3800"/>
    <path d="M140 153 Q166 128 198 133 Q228 139 238 118 Q252 96 271 100" fill="none" stroke="#fff" stroke-width="1.2"/>
  </svg>
  <p class="tagline" style="color:#fff">Cook, Learn. Repeat</p>
  <h1 class="center cover-title">Kitchen Duo<sup>TM</sup></h1>
  <p class="center cover-sub">Investor Overview | This document exists for<br><span class="accent">our future partners.</span></p>
  <div class="dots" style="left:17px;top:135px"><i></i><i class="on"></i><i></i></div>
</section>

<!-- 2 Cover light -->
<section class="slide c2 r1">
  <svg class="waves" viewBox="0 0 271 153" aria-hidden="true">
    <path d="M168 0 Q180 22 214 17 Q244 12 253 32 Q261 48 271 47 L271 0Z" fill="#ff3800"/>
    <path d="M172 0 Q184 18 214 13 Q244 8 253 27 Q261 42 271 41 L271 0Z" fill="#262626"/>
    <path d="M0 124 Q32 112 62 124 Q86 133 96 153 L0 153Z" fill="#ff3800"/>
    <path d="M0 128 Q32 118 60 128 Q82 136 90 153 L0 153Z" fill="#262626"/>
  </svg>
  <p class="tagline">Cook, Learn. Repeat</p>
  <h1 class="center cover-title" style="top:56px;font-size:20px">Kitchen Duo<sup>TM</sup></h1>
  <p class="pill">A New Cooking Platform</p>
  <div class="dots" style="left:12px;top:138px"><i></i><i class="on"></i><i></i></div>
</section>

<!-- 3 What is -->
<section class="slide c3 r1">
  <p class="tagline">Cook, Learn. Repeat</p>
  <p class="brand">Kitchen Duo</p>
  <h2 class="h" style="left:24px;top:60px;font-size:12px">What is</h2>
  <h2 class="h accent" style="left:24px;top:74px;font-size:15px">Kitchen Duo?</h2>
  <div class="lorem" style="left:146px;top:37px;width:102px">
    <p>Lorem ipsum dolor sit amet, consectetuer adipiscing elit, sed diam nonummy nibh euismod tincidunt ut laoreet dolore magna aliquam erat volutpat.</p>
    <p>Ut wisi enim ad minim veniam, quis nostrud exerci tation ullamcorper suscipit lobortis nisl ut aliquip ex ea commodo consequat. Duis autem vel eum iriure dolor in hendrerit in vulputate velit esse molestie consequat.</p>
    <p>Lorem ipsum dolor sit amet, consectetuer adipiscing elit, sed diam nonummy nibh euismod.</p>
  </div>
  <p class="confidential">Proprietary and Confidential</p>
  <div class="corner-mark"></div><p class="page-no">2</p>
</section>

<!-- 4 Consumer Insights -->
<section class="slide c1 r2">
  <p class="tagline">Cook, Learn. Repeat</p>
  <p class="brand">Kitchen Duo</p>
  <h2 class="h center" style="top:52px;font-size:17px">Consumer <span class="boxed">Insights</span></h2>
  <p class="center" style="top:85px;font-size:6.5px;font-weight:500">Text Added Here</p>
  <p class="lorem center" style="top:96px;padding:0 65px">Lorem ipsum dolor sit amet, consectetuer adipiscing elit, sed diam nonummy nibh euismod tincidunt ut laoreet dolore magna aliquam erat volutpat.</p>
  <p class="confidential">Proprietary and Confidential</p>
  <div class="corner-mark"></div><p class="page-no">3</p>
</section>

<!-- 5 Insight 1 -->
<section class="slide c2 r2">
  <p class="tagline">Cook, Learn. Repeat</p>
  <p class="brand">Kitchen Duo</p>
  <p class="insight-no">Insight 1</p>
  <div style="left:27px;top:33px">
    <p class="h" style="font-size:8px;font-weight:600">Growing Interest in</p>
    <p class="h accent" style="font-size:14px">Virtual Cooking</p>
    <p class="h" style="font-size:12px">Classes</p>
  </div>
  <div class="lorem" style="left:27px;top:82px;width:215px">
    <p>Lorem ipsum dolor sit amet, consectetuer adipiscing elit, sed diam nonummy nibh euismod tincidunt ut laoreet dolore magna aliquam erat volutpat. Ut wisi enim ad minim veniam, quis nostrud exerci tation ullamcorper suscipit lobortis nisl ut aliquip ex ea commodo consequat. Duis autem vel eum iriure dolor in hendrerit in vulputate velit esse molestie consequat.</p>
    <p>Lorem ipsum dolor sit amet, cons ectetuer adipiscing elit, sed diam nonummy nibh euismod tincidunt ut laoreet dolore magna aliquam erat volutpat.</p>
  </div>
  <p class="confidential">Proprietary and Confidential</p>
  <div class="corner-mark"></div><p class="page-no">4</p>
</section>

<!-- 6 Insight 2 -->
<section class="slide c3 r2">
  <p class="tagline">Cook, Learn. Repeat</p>
  <p class="brand">Kitchen Duo</p>
  <p class="insight-no">Insight 2</p>
  <div style="left:27px;top:33px">
    <p class="h" style="font-size:8px;font-weight:600">Demand for</p>
    <p class="h accent" style="font-size:13px">Interactive and Personalized</p>
    <p class="h" style="font-size:12px">Experience</p>
  </div>
  <div class="lorem" style="left:27px;top:82px;width:220px">
    <p>Lorem ipsum dolor sit amet, consectetuer adipiscing elit, sed diam nonummy nibh euismod tincidunt ut laoreet dolore magna aliquam erat volutpat. Ut wisi enim ad minim veniam, quis nostrud exerci tation ullamcorper suscipit lobortis nisl ut aliquip ex ea commodo consequat. Duis autem vel eum iriure dolor in hendrerit in vulputate velit esse molestie consequat.</p>
    <p>Lorem ipsum dolor sit amet, cons ectetuer adipiscing elit, sed diam nonummy nibh euismod tincidunt ut laoreet dolore magna aliquam erat volutpat.</p>
  </div>
  <p class="confidential">Proprietary and Confidential</p>
  <div class="corner-mark"></div><p class="page-no">5</p>
</section>

<!-- 7 Insight 3 -->
<section class="slide c1 r3">
  <p class="tagline">Cook, Learn. Repeat</p>
  <p class="brand">Kitchen Duo</p>
  <p class="insight-no">Insight 3</p>
  <div style="right:156px;top:56px;text-align:right">
    <p class="h" style="font-size:8px;font-weight:600">Global</p>
    <p class="h accent" style="font-size:14px">Cuisine</p>
    <p class="h" style="font-size:12px">Exploration</p>
  </div>
  <div class="lorem" style="left:127px;top:42px;width:110px">
    <p>Lorem ipsum dolor sit amet, consectetuer adipiscing elit, sed diam nonummy nibh euismod tincidunt ut laoreet dolore magna aliquam erat volutpat. Ut wisi enim ad minim veniam, quis nostrud exerci tation ullamcorper suscipit lobortis nisl ut aliquip ex ea commodo consequat. Duis autem vel eum iriure dolor in hendrerit in vulputate velit esse molestie consequat.</p>
    <p>Lorem ipsum dolor sit amet, cons ectetuer adipiscing elit, sed diam nonummy nibh euismod tincidunt ut laoreet dolore magna aliquam erat volutpat.</p>
  </div>
  <p class="confidential">Proprietary and Confidential</p>
  <div class="corner-mark"></div><p class="page-no">6</p>
</section>

<!-- 8 The Problem dark -->
<section class="slide dark c2 r3">
  <p class="tagline" style="color:#fff">Cook, Learn. Repeat</p>
  <p class="brand">Kitchen Duo</p>
  <h2 class="h center" style="top:57px;font-size:20px"><span class="boxed">The</span> Problem</h2>
  <p class="center accent" style="top:91px;font-size:5.4px;font-weight:500">Text Added Here</p>
  <p class="lorem center" style="top:100px;padding:0 75px">Lorem ipsum dolor sit amet, consectetuer adipiscing elit, sed diam nonummy nibh euismod tincidunt ut laoreet dolore magna aliquam erat volutpat.</p>
  <p class="confidential">Proprietary and Confidential</p>
  <div class="corner-mark"></div><p class="page-no">7</p>
</section>

<!-- 9 Problem stats -->
<section class="slide c3 r3">
  <p class="tagline">Cook, Learn. Repeat</p>
  <p class="brand">Kitchen Duo</p>
  <h2 class="h center" style="top:28px;font-size:11px">The <span class="accent">Problem</span></h2>
  <div class="lorem center" style="top:44px;padding:0 38px">
    <p>Lorem ipsum dolor sit amet, consectetuer adipiscing elit, sed diam nonummy nibh euismod tincidunt ut laoreet dolore magna aliquam erat volutpat.</p>
    <p>Lorem ipsum dolor sit amet, consectetuer adipiscing elit, sed diam nonummy nibh euismod tincidunt ut laoreet dolore magna aliquam erat volutpat.</p>
  </div>
  <div class="stats">
    <div class="stat"><b>768K</b><strong>Lorem Ipsum</strong><span>Lorem ipsum dolor sit amet, consectetuer elit.</span></div>
    <div class="stat"><b>423K</b><strong>Lorem Ipsum</strong><span>Lorem ipsum dolor sit amet, consectetuer elit.</span></div>
    <div class="stat"><b>135K</b><strong>Lorem Ipsum</strong><span>Lorem ipsum dolor sit amet, consectetuer elit.</span></div>
  </div>
  <p class="confidential">Proprietary and Confidential</p>
  <div class="corner-mark"></div><p class="page-no">8</p>
</section>

<!-- 10 Market Opportunity -->
<section class="slide c1 r4">
  <p class="tagline">Cook, Learn. Repeat</p>
  <p class="brand">Kitchen Duo</p>
  <h2 class="h" style="left:62px;top:46px;font-size:20px">Market</h2>
  <h2 class="h boxed" style="left:58px;top:73px;font-size:20px;padding:2px 4px">Opportunity</h2>
  <p class="confidential">Proprietary and Confidential</p>
  <div class="corner-mark"></div><p class="page-no">9</p>
</section>

<!-- 11 Consumer Insight 1 -->
<section class="slide c2 r4">
  <p class="tagline">Cook, Learn. Repeat</p>
  <p class="brand">Kitchen Duo</p>
  <p style="left:17px;top:30px;font-size:3.6px;font-weight:500">Consumer Insight 1</p>
  <div class="band" style="left:12px;top:74px;width:259px;height:13px"></div>
  <p class="accent" style="left:17px;top:47px;font-size:5.6px;font-weight:600">Increasing Demand</p>
  <p class="h" style="left:17px;top:55px;font-size:13px">For Healthier</p>
  <p class="h" style="left:17px;top:75.5px;font-size:10.5px;color:#fff">Home- Cooked</p>
  <p class="h" style="left:17px;top:88px;font-size:13px">Meals</p>
  <div class="card" style="left:124px;top:48px"><p class="card-head">Text Here</p><p class="lorem">Lorem ipsum dolor sit amet, consectetuer adipiscing elit, sed diam nonummy nibh euismod.<br><br>Ut wisi enim ad minim veniam, quis nostrud exerci tation.</p></div>
  <div class="card" style="left:194px;top:48px"><p class="card-head">Text Here</p><p class="lorem">Lorem ipsum dolor sit amet, consectetuer adipiscing elit, sed diam nonummy nibh euismod.<br><br>Ut wisi enim ad minim veniam, quis nostrud exerci tation.</p></div>
  <p class="confidential">Proprietary and Confidential</p>
  <div class="corner-mark"></div><p class="page-no">10</p>
</section>

<!-- 12 Consumer Insight 2 -->
<section class="slide c3 r4">
  <p class="tagline">Cook, Learn. Repeat</p>
  <p class="brand">Kitchen Duo</p>
  <p style="left:15px;top:30px;font-size:3.6px;font-weight:500">Consumer Insight 2</p>
  <p class="h" style="left:15px;top:44px;font-size:6.8px;font-weight:600">Convenience and</p>
  <div class="band" style="left:10px;top:55px;width:261px;height:23px"></div>
  <p class="h" style="left:15px;top:56px;font-size:19px;color:#fff">Time-Saving</p>
  <p class="h" style="left:15px;top:80px;font-size:13px">Solutions</p>
  <div class="card" style="left:166px;top:41px;width:61px"><p class="card-head">Text Here</p><p class="lorem">Lorem ipsum dolor sit amet, consectetuer adipiscing elit, sed diam nonummy nibh euismod.<br><br>Ut wisi enim ad minim veniam, quis nostrud exerci tation.</p></div>
  <p class="confidential">Proprietary and Confidential</p>
  <div class="corner-mark"></div><p class="page-no">11</p>
</section>

<!-- 13 Current Solutions -->
<section class="slide c1 r5">
  <p class="tagline">Cook, Learn. Repeat</p>
  <p class="brand">Kitchen Duo</p>
  <svg style="left:0;top:0" width="271" height="153" aria-hidden="true">
    <path d="M94 72 L105 58 L125 58 M96 80 L125 80 M94 88 L105 102 L125 102" fill="none" stroke="#333" stroke-width=".6"/>
  </svg>
  <div class="ring"><span>CURRENT</span><span class="accent">SOLUTIONS</span></div>
  <div class="item-icon" style="left:134px;top:31px"></div>
  <div class="item-text" style="left:157px;top:31px"><strong>Project name</strong><p class="lorem">Lorem ipsum dolor sit amet, nec an dictas equidem appellantur.</p></div>
  <div class="item-icon" style="left:134px;top:65px"></div>
  <div class="item-text" style="left:157px;top:65px"><strong>Project name</strong><p class="lorem">Lorem ipsum dolor sit amet, nec an dictas equidem appellantur.</p></div>
  <div class="item-icon" style="left:134px;top:100px"></div>
  <div class="item-text" style="left:157px;top:100px"><strong>Project name</strong><p class="lorem">Lorem ipsum dolor sit amet, nec an dictas equidem appellantur.</p></div>
  <p class="confidential">Proprietary and Confidential</p>
  <div class="corner-mark"></div><p class="page-no">12</p>
</section>

<!-- 14 A Better Solution -->
<section class="slide c2 r5">
  <p class="tagline">Cook, Learn. Repeat</p>
  <p class="brand">Kitchen Duo</p>
  <h2 class="h center" style="top:23px;font-size:10px">A Better <span class="accent">Solution</span></h2>
  <div class="step" style="left:56px"><b>IDEA</b><p class="lorem">Lorem ipsum dolor sit amet, consectetuer adipiscing elit, sed diam nonummy nibh euismod.</p></div>
  <div class="step" style="left:114px"><b>PROMOTION</b><p class="lorem">Lorem ipsum dolor sit amet, consectetuer adipiscing elit, sed diam nonummy nibh euismod.</p></div>
  <div class="step" style="left:172px"><b>GROWTH</b><p class="lorem">Lorem ipsum dolor sit amet, consectetuer adipiscing elit, sed diam nonummy nibh euismod.</p></div>
  <span class="node" style="left:97px;top:58px"></span>
  <span class="node" style="left:112px;top:93px"></span>
  <span class="node" style="left:155px;top:52px"></span>
  <span class="node" style="left:170px;top:99px"></span>
  <p class="lorem center" style="top:119px;padding:0 40px">Lorem ipsum dolor sit amet, consectetuer adipiscing elit, sed diam nonummy nibh euismod tincidunt ut laoreet dolore magna aliquam erat volutpat.</p>
  <p class="confidential">Proprietary and Confidential</p>
  <div class="corner-mark"></div><p class="page-no">13</p>
</section>

<!-- 15 Our Demo -->
<section class="slide c3 r5">
  <p class="tagline">Cook, Learn. Repeat</p>
  <p class="brand">Kitchen Duo</p>
  <h2 class="h" style="left:18px;top:35px;font-size:12px">Our <span class="accent">Demo</span></h2>
  <span class="num" style="left:23px;top:57px">1.</span>
  <div class="demo-item" style="left:37px;top:57px"><strong>Lorem Ipsum</strong><p class="lorem">Lorem ipsum dolor sit amet, consectetuer adipiscing elit.</p></div>
  <span class="num" style="left:23px;top:79px">2.</span>
  <div class="demo-item" style="left:37px;top:79px"><strong>Lorem Ipsum</strong><p class="lorem">Lorem ipsum dolor sit amet, consectetuer adipiscing elit.</p></div>
  <span class="num" style="left:23px;top:101px">3.</span>
  <div class="demo-item" style="left:37px;top:101px"><strong>Lorem Ipsum</strong><p class="lorem">Lorem ipsum dolor sit amet, consectetuer adipiscing elit.</p></div>
  <div class="phone" style="left:122px;top:28px">Lorem ipsum dolor<div class="glyph"></div><p class="lorem">Short text about the demo.</p></div>
  <div class="phone" style="left:158px;top:47px;height:56px">Dolor sit amet, conse<div class="glyph"></div><p class="lorem">Short text about the demo.</p></div>
  <div class="phone" style="left:195px;top:66px">Consec<div class="glyph"></div><p class="lorem">Short text about the demo.</p></div>
  <p class="confidential">Proprietary and Confidential</p>
  <div class="corner-mark"></div><p class="page-no">14</p>
</section>

<!-- 16 Timeline -->
<section class="slide c1 r6">
  <p class="tagline">Cook, Learn. Repeat</p>
  <p class="brand">Kitchen Duo</p>
  <h2 class="h" style="left:12px;top:31px;font-size:7.2px">Project <span class="accent">Timeline - 2024</span></h2>
  <p class="tl-note" style="left:25px;top:52px">Your Title<span>Refers to a good or service being offered</span></p>
  <p class="tl-note" style="left:104px;top:52px">Your Title<span>Refers to a good or service being offered</span></p>
  <p class="tl-note" style="left:183px;top:52px">Your Title<span>Refers to a good or service being offered</span></p>
  <span class="stem hot up" style="left:50px;top:75px;height:9px"></span>
  <span class="stem hot up" style="left:129px;top:75px;height:9px"></span>
  <span class="stem hot up" style="left:208px;top:75px;height:9px"></span>
  <p class="ribbon" style="left:30px;background:var(--orange)">1990</p>
  <p class="ribbon" style="left:69px;background:#1e1e1e">2001</p>
  <p class="ribbon" style="left:109px;background:var(--orange)">2007</p>
  <p class="ribbon" style="left:148px;background:#1e1e1e">2012</p>
  <p class="ribbon" style="left:188px;background:var(--orange)">2020</p>
  <span class="stem down" style="left:89px;top:90px;height:10px"></span>
  <span class="stem down" style="left:168px;top:90px;height:10px"></span>
  <p class="tl-note" style="left:64px;top:109px">Your Title<span>Refers to a good or service being offered</span></p>
  <p class="tl-note" style="left:143px;top:109px">Your Title<span>Refers to a good or service being offered</span></p>
  <p class="confidential">Proprietary and Confidential</p>
  <div class="corner-mark"></div><p class="page-no">15</p>
</section>

<!-- 17 Revenue Model -->
<section class="slide c2 r6">
  <p class="tagline">Cook, Learn. Repeat</p>
  <p class="brand">Kitchen Duo</p>
  <h2 class="h" style="left:12px;top:31px;font-size:7.5px">Revenue <span class="accent">Model</span></h2>
  <svg style="left:101px;top:53px" width="70" height="70" viewBox="0 0 70 70" aria-hidden="true">
    <path d="M35 1 A34 34 0 0 1 69 35 L52 35 A17 17 0 0 0 35 18Z" fill="#1e1e1e"/>
    <path d="M69 35 A34 34 0 0 1 35 69 L35 52 A17 17 0 0 0 52 35Z" fill="#ff3800"/>
    <path d="M35 69 A34 34 0 0 1 1 35 L18 35 A17 17 0 0 0 35 52Z" fill="#1e1e1e"/>
    <path d="M1 35 A34 34 0 0 1 35 1 L35 18 A17 17 0 0 0 18 35Z" fill="#ff3800"/>
    <path d="M35 0V70M0 35H70" stroke="#fefefa" stroke-width="1.5"/>
    <circle cx="35" cy="35" r="17" fill="#fefefa"/>
    <circle cx="20" cy="20" r="4" fill="none" stroke="#fff" stroke-width=".8"/>
    <circle cx="50" cy="20" r="4" fill="none" stroke="#fff" stroke-width=".8"/>
    <circle cx="20" cy="50" r="4" fill="none" stroke="#fff" stroke-width=".8"/>
    <circle cx="50" cy="50" r="4" fill="none" stroke="#fff" stroke-width=".8"/>
  </svg>
  <p class="h center" style="top:80px;font-size:6.4px;font-weight:600">Text<br>Added</p>
  <div class="rev left" style="left:23px;top:53px">Text Here<p class="lorem">Lorem ipsum dolor sit amet, consectetuer adipiscing elit, sed diam nonummy nibh euismod.</p></div>
  <div class="rev" style="left:176px;top:53px"><span class="accent">Text Here</span><p class="lorem">Lorem ipsum dolor sit amet, consectetuer adipiscing elit, sed diam nonummy nibh euismod.</p></div>
  <div class="rev left" style="left:23px;top:102px"><span class="accent">Text Here</span><p class="lorem">Lorem ipsum dolor sit amet, consectetuer adipiscing elit, sed diam nonummy nibh euismod.</p></div>
  <div class="rev" style="left:176px;top:102px">Text Here<p class="lorem">Lorem ipsum dolor sit amet, consectetuer adipiscing elit, sed diam nonummy nibh euismod.</p></div>
  <p class="confidential">Proprietary and Confidential</p>
  <div class="corner-mark"></div><p class="page-no">16</p>
</section>

<!-- 18 Financial Projections -->
<section class="slide c3 r6">
  <p class="tagline">Cook, Learn. Repeat</p>
  <p class="brand">Kitchen Duo</p>
  <h2 class="h center" style="top:36px;font-size:7.5px">Financial <span class="accent">Projections.</span></h2>
  <svg style="left:28px;top:52px" width="215" height="25" viewBox="0 0 215 25" aria-hidden="true">
    <g font-family="Poppins, sans-serif" font-size="5" font-weight="600" fill="#fff" text-anchor="middle">
      <path d="M0 0H38L46 12.5L38 25H0L8 12.5Z" fill="#1e1e1e"/><text x="24" y="14.5">2024</text>
      <path d="M41 0H79L87 12.5L79 25H41L49 12.5Z" fill="#ff3800"/><text x="65" y="14.5">2025</text>
      <path d="M82 0H120L128 12.5L120 25H82L90 12.5Z" fill="#1e1e1e"/><text x="106" y="14.5">2026</text>
      <path d="M123 0H161L169 12.5L161 25H123L131 12.5Z" fill="#ff3800"/><text x="147" y="14.5">2027</text>
      <path d="M164 0H202L210 12.5L202 25H164L172 12.5Z" fill="#1e1e1e"/><text x="188" y="14.5">2028</text>
    </g>
  </svg>
  <div class="proj" style="left:31px;top:84px">Project name<p class="lorem">Lorem Ipsum is simply dummy unknown printer took a galley of type and scrambled it to make.</p></div>
  <div class="proj accent" style="left:72px;top:84px">Project name<p class="lorem">Lorem Ipsum is simply dummy unknown printer took a galley of type and scrambled it to make.</p></div>
  <div class="proj" style="left:113px;top:84px">Project name<p class="lorem">Lorem Ipsum is simply dummy unknown printer took a galley of type and scrambled it to make.</p></div>
  <div class="proj accent" style="left:154px;top:84px">Project name<p class="lorem">Lorem Ipsum is simply dummy unknown printer took a galley of type and scrambled it to make.</p></div>
  <div class="proj" style="left:195px;top:84px">Project name<p class="lorem">Lorem Ipsum is simply dummy unknown printer took a galley of type and scrambled it to make.</p></div>
  <p class="confidential">Proprietary and Confidential</p>
  <div class="corner-mark"></div><p class="page-no">17</p>
</section>

<!-- 19 The Ask -->
<section class="slide c1 r7">
  <p class="tagline">Cook, Learn. Repeat</p>
  <p class="brand">Kitchen Duo</p>
  <h2 class="h" style="left:24px;top:40px;font-size:13px">The <span class="accent">Ask.</span></h2>
  <div class="bullet" style="left:34px;top:66px">Lorem ipsum<p class="lorem">Lorem ipsum dolor sit amet, consectetuer adipiscing elit, sed diam nonummy nibh.</p></div>
  <div class="bullet" style="left:34px;top:88px">Lorem ipsum<p class="lorem">Lorem ipsum dolor sit amet, consectetuer adipiscing elit, sed diam nonummy nibh.</p></div>
  <div class="ph" role="img" aria-label="Desktop monitor showing the deck cover slide" style="left:120px;top:26px;width:116px;height:96px;border-radius:3px"></div>
  <p style="left:178px;top:93px;background:var(--orange);color:#fff;font-size:4.6px;font-weight:600;padding:1px 6px">Text Added Here</p>
  <p class="confidential">Proprietary and Confidential</p>
  <div class="corner-mark"></div><p class="page-no">18</p>
</section>

<!-- 20 The Team -->
<section class="slide c2 r7">
  <p class="tagline">Cook, Learn. Repeat</p>
  <p class="brand">Kitchen Duo</p>
  <h2 class="h center" style="top:36px;font-size:10.5px">The <span class="accent">Team</span></h2>
  <div class="member" style="left:25px"><div class="strip" style="background:#1e1e1e"><div class="face" role="img" aria-label="Portrait photo of team member"></div></div><h4 class="accent">JOHN SMITH</h4><p class="lorem">Lorem ipsum dolor sit amet, consectetuer adipiscing elit.</p></div>
  <div class="member" style="left:85px"><div class="strip" style="background:var(--orange)"><div class="face" role="img" aria-label="Portrait photo of team member"></div></div><h4>MILLIE SMITH</h4><p class="lorem">Lorem ipsum dolor sit amet, consectetuer adipiscing elit.</p></div>
  <div class="member" style="left:145px"><div class="strip" style="background:#1e1e1e"><div class="face" role="img" aria-label="Portrait photo of team member"></div></div><h4 class="accent">JOHN SMITH</h4><p class="lorem">Lorem ipsum dolor sit amet, consectetuer adipiscing elit.</p></div>
  <div class="member" style="left:206px"><div class="strip" style="background:var(--orange)"><div class="face" role="img" aria-label="Portrait photo of team member"></div></div><h4>MILLIE SMITH</h4><p class="lorem">Lorem ipsum dolor sit amet, consectetuer adipiscing elit.</p></div>
  <p class="confidential">Proprietary and Confidential</p>
  <div class="corner-mark"></div><p class="page-no">19</p>
</section>

<!-- 21 Thank You dark -->
<section class="slide dark c3 r7">
  <p class="tagline" style="color:#fff">Cook, Learn. Repeat</p>
  <p class="brand">Kitchen Duo</p>
  <div role="img" aria-label="Cartoon chef character holding a spatula and fork" style="left:25px;top:30px;width:118px;height:123px;background:linear-gradient(170deg,#f4f4f2 0%,#d9d9d6 60%,#c0392b 100%);opacity:.9;border-radius:50px 50px 0 0"></div>
  <h2 class="h accent" style="left:146px;top:43px;font-size:17px">Thank You</h2>
  <div class="contact" style="top:73px">
    <svg viewBox="0 0 24 24" aria-hidden="true"><path fill="#ff3800" d="M6.6 10.8a15 15 0 0 0 6.6 6.6l2.2-2.2c.3-.3.7-.4 1-.2 1.1.4 2.3.6 3.6.6.6 0 1 .4 1 1V20c0 .6-.4 1-1 1A17 17 0 0 1 3 4c0-.6.4-1 1-1h3.5c.6 0 1 .4 1 1 0 1.3.2 2.5.6 3.6.1.3 0 .7-.2 1z"/></svg>
    <p>+10 5550 1234 5678<br>+10 5550 1234 5678</p>
  </div>
  <div class="contact" style="top:89px">
    <svg viewBox="0 0 24 24" aria-hidden="true"><path fill="#ff3800" d="M2 21l21-9L2 3v7l15 2-15 2z"/></svg>
    <p>www.kitchenduo.example<br>hello@kitchenduo.example</p>
  </div>
  <div class="contact" style="top:103px">
    <svg viewBox="0 0 24 24" aria-hidden="true"><path fill="#ff3800" d="M12 3L2 12h3v8h5v-6h4v6h5v-8h3z"/></svg>
    <p>88 Harbor Lane, Millbrook,<br>State 40210.</p>
  </div>
  <p class="confidential">Proprietary and Confidential</p>
  <div class="corner-mark"></div><p class="page-no">20</p>
</section>

</main>
</body>
</html>
```